One of Australia's fastest growing Financial Company looking for an updated business card design!

Meridale Partners Australia is looking for an updated design for our business cards. We would like to keep up our professional appearances and have get new exciting design that fits our company.

The Meridale aim is to facilitate and assist clients in every financial requirement that may arise in financial areas.

We would to see the design to use colour blue and we like the clouds in the background. We have attached two designs we have use before but we need something with more professional and easy to read design.

We would like the website in the back of the card; the employees name more central and stands out; only a postal address; a list of all our locations along the bottom (Sydney, Melbourne, Brisbane, Singapore)

Looking forward to seeing the designs come in!

Target Market(s)

Other Industry Professionals
Middle Class Families

Industry/Entity Type

Finance

Contact Information for Business Card

Name; Company Role; Office Number; Mobile Number; Email Address; Website; Postal Address; Locations

Font styles to use
Serif
Sans Serif

Colors
0492cd
33a6d7
85cae6
85acd3
3176b5
0455a3
cee9f5
d5e2ee

Requirements
Must have
• Name; Company Role; Office Number; Mobile Number; Email Address; Website; Postal Address; Locations
Nice to have
• The colour blue, clouds on the background

```html
<!DOCTYPE html>
<html lang="en">
<head>
<meta charset="utf-8">
<title>Meridale Partners Australia – Business Card</title>
<link rel="stylesheet" href="https://fonts.googleapis.com/css2?family=Open+Sans:wght@400;600;700;800&display=swap">
<style>
  :root {
    --navy: #1a4f98;
    --steel: #3176b5;
    --steel-soft: #3a7db9;
    --cyan: #2a90c8;
    --sky-deep: #85cae6;
    --sky-light: #cee9f5;
    --mist: #d5e2ee;
    --page: #ececed;
    --white: #ffffff;
    --icon-bg: rgba(255,255,255,0.16);
  }
  * { box-sizing: border-box; margin: 0; padding: 0; }
  html, body { width: 1200px; height: 900px; overflow: hidden; }
  body {
    background: var(--page);
    font-family: "Open Sans", Arial, sans-serif;
    position: relative;
  }
  .card {
    position: absolute;
    top: 291px;
    width: 520px;
    height: 318px;
    overflow: hidden;
    box-shadow: 0 10px 24px rgba(0,0,0,0.18);
  }
  .card--front { left: 50px; background: var(--navy); }
  .card--back { left: 630px; }

  /* front */
  .brand-block {
    position: absolute; left: 34px; top: 58px;
    display: flex; align-items: center; gap: 18px;
  }
  .wordmark {
    display: flex; align-items: center; gap: 7px;
    color: var(--white); font-weight: 600; font-size: 22px;
  }
  .wordmark__dot { width: 12px; height: 12px; border-radius: 50%; background: var(--white); }
  .divider { width: 1px; height: 58px; background: rgba(255,255,255,0.7); }
  .person__name { color: var(--white); font-weight: 800; font-size: 27px; line-height: 1.05; }
  .person__role { color: var(--white); font-weight: 700; font-size: 11.5px; line-height: 1.2; text-transform: uppercase; }

  .band { position: absolute; left: 0; width: 100%; }
  .band--contact { top: 160px; height: 50px; background: var(--steel); }
  .band--address { top: 210px; height: 44px; background: var(--cyan); }
  .band--gap { top: 254px; height: 14px; background: var(--steel-soft); }
  .band--cities { top: 268px; height: 50px; background: var(--cyan); }

  .contact-item {
    position: absolute; color: var(--white);
    font-size: 12.5px; white-space: nowrap;
  }
  .contact-item .icon {
    position: absolute; left: 50%; top: -30px; transform: translateX(-50%);
    width: 28px; height: 28px; border-radius: 50%; background: var(--icon-bg);
    display: flex; align-items: center; justify-content: center;
  }
  .cities {
    position: absolute; inset: 0; display: flex; align-items: center; justify-content: center;
    color: var(--white); font-size: 13px; letter-spacing: 3px; text-transform: uppercase;
  }

  /* back */
  .sky {
    position: absolute; inset: 0;
    background:
      radial-gradient(ellipse at 42% 58%, var(--white) 0%, rgba(255,255,255,0.8) 22%, rgba(255,255,255,0) 55%),
      linear-gradient(180deg, var(--sky-deep) 0%, var(--sky-light) 65%, var(--mist) 100%);
  }
  .back-brand {
    position: absolute; left: 0; right: 0; top: 118px;
    display: flex; justify-content: center; align-items: center; gap: 9px;
    color: var(--cyan); font-weight: 600; font-size: 40px;
  }
  .back-brand__dot { width: 18px; height: 18px; border-radius: 50%; background: var(--cyan); }
  .band--web { top: 232px; height: 50px; background: var(--cyan); }
  .band--base { top: 282px; height: 36px; background: var(--steel); }
  .web {
    position: absolute; inset: 0; display: flex; align-items: center; justify-content: center;
    color: var(--white); font-size: 16px;
  }
  .globe {
    position: absolute; right: 150px; top: -16px;
    width: 30px; height: 30px; border-radius: 50%; background: var(--steel);
    display: flex; align-items: center; justify-content: center;
  }
</style>
</head>
<body>

<section class="card card--front">
  <div class="brand-block">
    <div class="wordmark"><span class="wordmark__dot"></span>Meridale</div>
    <div class="divider"></div>
    <div class="person">
      <div class="person__name">Daniel Hart</div>
      <div class="person__role">Manager</div>
      <div class="person__role">Premium Banking Services</div>
    </div>
  </div>

  <div class="band band--contact">
    <div class="contact-item" style="left:24px; top:18px;">
      <span class="icon"><svg width="14" height="11" viewBox="0 0 14 11"><rect x="0.5" y="0.5" width="13" height="10" fill="none" stroke="#fff"/><path d="M0.5 0.5 L7 6 L13.5 0.5" fill="none" stroke="#fff"/></svg></span>
      daniel@mpaus.com.au
    </div>
    <div class="contact-item" style="left:225px; top:18px;">
      <span class="icon"><svg width="10" height="15" viewBox="0 0 10 15"><rect x="0.5" y="0.5" width="9" height="14" rx="1.5" fill="none" stroke="#fff"/><circle cx="5" cy="12" r="0.9" fill="#fff"/></svg></span>
      0400 318
    </div>
    <div class="contact-item" style="left:425px; top:18px;">
      <span class="icon"><svg width="14" height="14" viewBox="0 0 14 14"><path d="M3 1 L5.5 4 L4 5.5 C5 7.5 6.5 9 8.5 10 L10 8.5 L13 11 L11 13 C6 12.5 1.5 8 1 3 Z" fill="none" stroke="#fff"/></svg></span>
      (02) 5550
    </div>
  </div>

  <div class="band band--address">
    <div class="contact-item" style="left:24px; top:14px;">
      <span class="icon" style="top:-29px;"><svg width="11" height="15" viewBox="0 0 11 15"><path d="M5.5 14 C2 9 1 7 1 5 A4.5 4.5 0 0 1 10 5 C10 7 9 9 5.5 14 Z" fill="none" stroke="#fff"/><circle cx="5.5" cy="5" r="1.6" fill="none" stroke="#fff"/></svg></span>
      Level 6, Ridge Dve, Oakmere, NSW 2150
    </div>
    <div class="contact-item" style="left:268px; top:14px;">
      <span class="icon" style="top:-29px;"><svg width="14" height="13" viewBox="0 0 14 13"><path d="M1 7 V12 H13 V7" fill="none" stroke="#fff"/><path d="M7 9 V1 M4 4 L7 1 L10 4" fill="none" stroke="#fff"/></svg></span>
      PO Box 0000 Harwood Hills, NSW 2150
    </div>
  </div>

  <div class="band band--gap"></div>

  <div class="band band--cities">
    <div class="cities">Sydney | Melbourne | Brisbane | Singapore</div>
  </div>
</section>

<section class="card card--back">
  <div class="sky" role="img" aria-label="Bright blue sky with sunlit white clouds"></div>
  <div class="back-brand"><span class="back-brand__dot"></span>Meridale</div>
  <div class="band band--web">
    <span class="globe"><svg width="18" height="18" viewBox="0 0 18 18"><circle cx="9" cy="9" r="7.5" fill="none" stroke="#fff"/><ellipse cx="9" cy="9" rx="3.5" ry="7.5" fill="none" stroke="#fff"/><path d="M1.5 9 H16.5 M3 5 H15 M3 13 H15" stroke="#fff" fill="none"/></svg></span>
    <div class="web">www.meridalepartnersaustralia.com.au</div>
  </div>
  <div class="band band--base"></div>
</section>

</body>
</html>
```